business card for larch cove dental arts
Larch Cove Dental Arts
Professional
Rowland K. Bevacquist DDS
4 Mossbank Ln
Larch Cove, NY 14093
larchcovedentalarts@mailvane.example
larchcovedentalarts.example
On the card either at the bottom or the top I would like it to say "Implants Family Dentistry Cosmetic Dentistry" to tell people what i offer, or as a motto
________ ______ has an appointment
___/___/___@ ___:___am/pm
Mon Tues Wed Thurs Fri Sat
Logo design
the white may be easier to work with for the card

```html
<!DOCTYPE html>
<html lang="en">
<head>
<meta charset="utf-8">
<title>Larch Cove Dental Arts – Business Card</title>
<link rel="stylesheet" href="https://fonts.googleapis.com/css2?family=Libre+Baskerville:ital,wght@0,400;1,700&family=Open+Sans:ital,wght@0,400;0,600;1,400&display=swap">
<style>
  :root {
    --page: #ecebe8;
    --card: #ffffff;
    --ink: #2b2b2b;
    --muted: #555555;
    --accent-blue: #4a74c4;
    --accent-orange: #e9963c;
    --accent-purple: #8d6bb5;
    --rule: #8a8a8a;
    --mark-fill: #e6e3ef;
  }
  * { box-sizing: border-box; margin: 0; padding: 0; }
  html, body { width: 1200px; height: 402px; overflow: hidden; }
  body { background: var(--page); position: relative; font-family: "Open Sans", Arial, sans-serif; color: var(--ink); }

  .card {
    position: absolute; top: 24px; width: 558px; height: 354px;
    background: var(--card); box-shadow: 0 2px 6px rgba(0,0,0,.18);
  }
  .card--front { left: 28px; }
  .card--back { left: 614px; }

  /* Front */
  .brand { position: absolute; left: 36px; top: 40px; width: 200px; text-align: center; }
  .brand__dot { width: 84px; height: 84px; border-radius: 50%; background: var(--mark-fill); margin: 0 auto 16px; }
  .brand__name { font-family: "Open Sans", Arial, sans-serif; font-weight: 600; color: var(--ink); font-size: 22px; line-height: 1.3; }

  .contact { position: absolute; right: 26px; top: 200px; width: 268px; text-align: right; }
  .contact__name { font-size: 16px; font-weight: 600; border-bottom: 1px solid var(--rule); padding-bottom: 4px; margin-bottom: 8px; }
  .contact__name small { font-size: 11px; font-weight: 400; }
  .contact__line { display: flex; justify-content: flex-end; align-items: center; gap: 6px; font-size: 12px; color: var(--muted); line-height: 20px; }
  .contact__line svg { width: 12px; height: 12px; flex: none; }
  .contact__address { font-size: 12px; color: var(--muted); margin-top: 2px; }

  /* Back */
  .services { position: absolute; left: 26px; top: 22px; font-family: "Libre Baskerville", Georgia, serif; font-style: italic; font-weight: 700; font-size: 15px; }
  .appt__title { position: absolute; left: 26px; top: 62px; font-family: "Libre Baskerville", Georgia, serif; font-weight: 400; font-size: 21px; }
  .appt__field { position: absolute; left: 26px; font-size: 12.5px; display: flex; align-items: flex-end; gap: 6px; }
  .dots { border-bottom: 1.5px dotted var(--muted); height: 12px; }
  .slot { width: 72px; height: 20px; border: 1px solid var(--accent-blue); }
  .days { position: absolute; left: 26px; top: 280px; display: flex; gap: 9px; }
  .day { display: flex; align-items: center; gap: 4px; color: var(--accent-blue); font-weight: 600; font-size: 12.5px; }
  .day span { width: 24px; height: 16px; border: 1px solid var(--accent-blue); }
  .notice { position: absolute; left: 26px; top: 312px; font-size: 12px; font-style: italic; color: var(--muted); }
  .back-brand { position: absolute; right: 26px; top: 66px; width: 130px; text-align: center; }
  .back-brand__dot { width: 70px; height: 70px; border-radius: 50%; background: var(--mark-fill); margin: 0 auto 8px; }
  .back-brand__name { font-weight: 600; font-size: 13px; line-height: 1.3; color: var(--ink); }
</style>
</head>
<body>

<section class="card card--front" aria-label="Card front">
  <div class="brand">
    <div class="brand__dot"></div>
    <p class="brand__name">Larch Cove<br>Dental Arts</p>
  </div>

  <div class="contact">
    <p class="contact__name">Rowland K. Bevacquist, <small>DDS</small></p>
    <p class="contact__line">
      <svg viewBox="0 0 16 16"><path fill="var(--accent-orange)" d="M3.6 1.5l2.3 2.6-1.3 1.8c.9 2 2.5 3.6 4.5 4.5l1.8-1.3 2.6 2.3-1.4 2.1C6.9 14.6 1.4 9.1 1.5 2.9z"/></svg>
      845-555-0147
    </p>
    <p class="contact__line">
      <svg viewBox="0 0 16 16"><rect x="1" y="3" width="14" height="10" rx="1" fill="var(--accent-purple)"/><path d="M1.5 3.8L8 9l6.5-5.2" stroke="#fff" fill="none"/></svg>
      larchcovedentalarts@mailvane.example
    </p>
    <p class="contact__line">
      <svg viewBox="0 0 16 16"><circle cx="8" cy="8" r="7" fill="var(--accent-orange)"/><path d="M1 8h14M8 1c-3 3-3 11 0 14M8 1c3 3 3 11 0 14" stroke="#fff" fill="none"/></svg>
      larchcovedentalarts.example
    </p>
    <p class="contact__address">4 Mossbank Ln, Larch Cove, NY 14093</p>
  </div>
</section>

<section class="card card--back" aria-label="Card back">
  <p class="services">Implants Family Dentistry, Cosmetic Dentistry</p>
  <h1 class="appt__title">YOUR APPOINTMENT</h1>

  <div class="appt__field" style="top:128px">Name :<span class="dots" style="width:220px"></span></div>
  <div class="appt__field" style="top:166px">Date :<span class="dots" style="width:96px"></span>Time :<span class="dots" style="width:86px"></span>am / pm</div>
  <div class="appt__field" style="top:208px;align-items:center">Next Appointment<span class="slot" style="margin-left:12px"></span><span class="slot" style="margin-left:8px"></span></div>

  <div class="days">
    <div class="day">MON<span></span></div>
    <div class="day">TUE<span></span></div>
    <div class="day">WED<span></span></div>
    <div class="day">THU<span></span></div>
    <div class="day">FRI<span></span></div>
    <div class="day">SAT<span></span></div>
  </div>

  <p class="notice">We appreciate a 24 hr. notice for cancellations</p>

  <div class="back-brand">
    <div class="back-brand__dot"></div>
    <p class="back-brand__name">Larch Cove<br>Dental Arts</p>
  </div>
</section>

</body>
</html>
```